Global Outreach Fellowship needs a Book Cover Design Project

I am a pastor, missionary, author, and the founder of a non-profit organization. I am in the process of publishing a book focused on "The Soul of a Faithful Shepherd" and desire a contemporary, even somewhat abstract book cover. Here is a link to the company's web page portfolio that designed our Web Page, to give you an idea of the style of cover that I am looking for. http://www.pixelharborstudio.com/cd-covers

Though the book is obviously targeted toward Christians, I want it to be attractive enough to capture the attention of the general population as well.

Industry/Entity Type

Non-Profit

```html
<!DOCTYPE html>
<html lang="en">
<head>
<meta charset="utf-8">
<title>The Soul of a Faithful Shepherd — Book Cover</title>
<link href="https://fonts.googleapis.com/css2?family=EB+Garamond:wght@400;500&display=swap" rel="stylesheet">
<style>
  :root {
    --page: #ffffff;
    --ink-light: #f4efe6;
    --band: rgba(8, 6, 5, 0.72);
    --deep: #120e0b;
    --umber: #3a2a1c;
    --rust: #7a3a1c;
    --amber: #c98a2e;
    --gold: #b8954e;
    --moss: #2b3526;
    --rule: #e9e4da;
    --barcode-box: #ffffff;
  }
  * { margin: 0; padding: 0; box-sizing: border-box; }
  html, body {
    width: 1200px; height: 949px; overflow: hidden;
    background: var(--page);
    font-family: "EB Garamond", Garamond, serif;
  }
  .cover-spread {
    position: absolute; left: 58px; top: 58px;
    width: 1100px; height: 820px;
    background: var(--deep);
    box-shadow: 0 4px 10px rgba(0,0,0,0.35);
    overflow: hidden;
  }
  .artwork { position: absolute; top: 0; height: 100%; }
  .artwork--back {
    left: 0; width: 530px;
    background:
      radial-gradient(ellipse 300px 240px at 300px 640px, var(--amber) 0%, var(--rust) 40%, transparent 75%),
      radial-gradient(ellipse 320px 300px at 230px 250px, #4a3a30 0%, transparent 70%),
      linear-gradient(160deg, #3b302a 0%, var(--umber) 45%, #1c1713 100%);
  }
  .artwork--spine {
    left: 530px; width: 38px;
    background: linear-gradient(180deg, #3a3a34 0%, #2a2019 50%, #4a3824 100%);
  }
  .artwork--front {
    left: 568px; width: 532px;
    background:
      radial-gradient(ellipse 170px 180px at 250px 150px, var(--gold) 0%, #8a6a32 45%, transparent 80%),
      radial-gradient(ellipse 260px 260px at 420px 700px, var(--moss) 0%, transparent 75%),
      linear-gradient(180deg, #2a2118 0%, #15110d 60%, #1d1e17 100%);
  }
  .spine-rule {
    position: absolute; top: 0; width: 2px; height: 100%;
    background: var(--rule);
  }
  .spine-rule--left { left: 529px; }
  .spine-rule--right { left: 567px; }
  .text-band {
    position: absolute; top: 298px; height: 280px;
    background: var(--band);
  }
  .text-band--back { left: 0; width: 529px; }
  .text-band--front { left: 569px; width: 531px; }
  .back-blurb {
    position: absolute; left: 50px; top: 328px; width: 430px;
    color: var(--ink-light);
    font-size: 15.4px; line-height: 19.3px;
  }
  .barcode-area {
    position: absolute; left: 48px; top: 694px;
    width: 175px; height: 94px;
    background: var(--barcode-box);
  }
  .spine-title {
    position: absolute; left: 549px; top: 300px;
    transform: translateX(-50%) rotate(90deg);
    transform-origin: center;
    width: 280px; text-align: center;
    translate: 0 110px;
    color: var(--ink-light);
    font-size: 18px; white-space: nowrap;
  }
  .book-title {
    position: absolute; left: 690px; top: 330px; width: 330px;
    color: var(--ink-light); text-align: center;
    font-weight: 400; line-height: 1;
  }
  .book-title .t-small { display: block; font-size: 34px; margin-left: 40px; }
  .book-title .t-large { display: block; font-size: 72px; margin-top: -12px; }
  .book-title .t-mid { display: block; font-size: 44px; margin-top: -4px; }
  .book-title .t-mid small { font-size: 30px; }
  .book-title .t-last { display: block; font-size: 56px; margin-top: 4px; }
  .author-name {
    position: absolute; left: 568px; width: 532px; top: 758px;
    text-align: center; color: var(--ink-light);
    font-size: 24px; letter-spacing: 4px;
  }
</style>
</head>
<body>
  <main class="cover-spread">
    <div class="artwork artwork--back" role="img" aria-label="Abstract textured painting in dark browns with a warm amber glow"></div>
    <div class="artwork artwork--spine" role="img" aria-label="Textured dark spine artwork"></div>
    <div class="artwork artwork--front" role="img" aria-label="Abstract textured artwork of golden stone-like hands on a dark background"></div>

    <div class="spine-rule spine-rule--left"></div>
    <div class="spine-rule spine-rule--right"></div>

    <div class="text-band text-band--back"></div>
    <div class="text-band text-band--front"></div>

    <p class="back-blurb">Lorem ipsum dolor sit amet, consectetur adipisicing elit, sed do eiusmod tempor incididunt ut labore et dolore magna aliqua. Ut enim ad minim veniam, quis nostrud exercitation ullamco laboris nisi ut aliquip ex ea commodo consequat. Duis aute irure dolor in reprehenderit in voluptate velit esse cillum dolore eu fugiat nulla pariatur. Excepteur sint occaecat cupidatat non proident, sunt in culpa qui officia deserunt mollit anim id est laborum. Lorem ipsum dolor sit amet, consectetur adipisicing elit, sed do eiusmod tempor incididunt ut labore et dolore magna aliqua. Ut enim ad minim veniam, quis nostrud exercitation ullamco laboris nisi ut aliquip ex ea commodo consequat. Duis aute irure dolor in reprehenderit.</p>

    <div class="barcode-area"></div>

    <p class="spine-title">The Soul of a Faithful Shepherd</p>

    <h1 class="book-title">
      <span class="t-small">The</span>
      <span class="t-large">Soul</span>
      <span class="t-mid"><small>of a</small> Faithful</span>
      <span class="t-last">Shepherd</span>
    </h1>

    <p class="author-name">Authors Name Here</p>
  </main>
</body>
</html>
```